Email Signatures

I would like to create a new email signature for my team. The design will be the same for everyone, with only individual details such as name and email changing. You can also see our brand style on our website. https://www.wlhtimberworks.com.au/

Target Market(s)

Clients for new builds or renovations

Industry/Entity Type

Construction

Colors

Designer to choose colors to be used in the design.

```html
<!DOCTYPE html>
<html lang="en">
<head>
<meta charset="utf-8">
<title>WLH Timber Works – Email Signature</title>
<link href="https://fonts.googleapis.com/css2?family=Montserrat:wght@800&family=Kumbh+Sans:wght@300;400&display=swap" rel="stylesheet">
<style>
  :root {
    --brand-green: #077940;
    --accent-green: #4caf50;
    --sheet-grey: #cccccc;
    --ink: #2a2623;
    --paper: #ffffff;
    --social-text: #cfe6d8;
  }
  * { margin: 0; padding: 0; box-sizing: border-box; }
  html, body { width: 958px; height: 1200px; overflow: hidden; }
  body { position: relative; font-family: "Kumbh Sans", sans-serif; color: var(--ink); background: var(--sheet-grey); }

  .backdrop-green { position: absolute; left: 0; top: 0; width: 958px; height: 599px; background: var(--brand-green); }
  .backdrop-grey { position: absolute; left: 0; top: 599px; width: 958px; height: 601px; background: var(--sheet-grey); }

  .signature {
    position: absolute; left: 137px; width: 684px; height: 205px;
    background: var(--paper);
    box-shadow: 2px 3px 4px rgba(0,0,0,0.28);
  }
  .signature--on-green { top: 197px; }
  .signature--on-grey { top: 795px; }

  .brand-mark { position: absolute; left: 44px; top: 72px; display: flex; align-items: center; gap: 8px; }
  .brand-mark__square { width: 14px; height: 14px; background: var(--brand-green); }
  .brand-mark__name { font-family: "Montserrat", sans-serif; font-weight: 800; font-size: 19px; line-height: 1.1; color: var(--ink); }

  .person-name {
    position: absolute; left: 224px; top: 22px;
    font-family: "Montserrat", sans-serif; font-weight: 800; font-size: 21px; letter-spacing: -0.2px;
  }
  .divider { position: absolute; left: 224px; right: 0; top: 50px; height: 2px; background: var(--accent-green); }
  .job-title { position: absolute; left: 224px; top: 56px; font-size: 13px; font-weight: 300; letter-spacing: 0.4px; }

  .contact-list { list-style: none; }
  .contact-item { position: absolute; left: 229px; font-size: 12px; font-weight: 400; line-height: 19px; }
  .contact-item svg { position: absolute; left: 0; top: 4px; width: 11px; height: 11px; fill: var(--ink); }
  .contact-item span { position: absolute; left: 14px; white-space: nowrap; }
  .contact-item--phone { top: 79px; }
  .contact-item--mail { top: 102px; }
  .contact-item--web { top: 125px; }
  .contact-item--address { top: 151px; }

  .social-panel { position: absolute; left: 528px; top: 52px; width: 156px; height: 153px; background: var(--brand-green); }
  .social-item { position: absolute; left: 23px; display: flex; align-items: center; gap: 7px; font-size: 9px; font-weight: 300; color: var(--social-text); letter-spacing: 0.3px; }
  .social-item__icon { width: 15px; height: 15px; border-radius: 3px; background: var(--paper); }
  .social-item:nth-child(1) { top: 56px; }
  .social-item:nth-child(2) { top: 76px; }
  .social-item:nth-child(3) { top: 96px; }
  .social-item:nth-child(4) { top: 116px; }
</style>
</head>
<body>
  <div class="backdrop-green"></div>
  <div class="backdrop-grey"></div>

  <section class="signature signature--on-green">
    <div class="brand-mark"><div class="brand-mark__square"></div><div class="brand-mark__name">WLH<br>Timber Works</div></div>
    <h1 class="person-name">SURENAME</h1>
    <div class="divider"></div>
    <p class="job-title">MANAGING DIRECTOR</p>
    <ul class="contact-list">
      <li class="contact-item contact-item--phone"><svg viewBox="0 0 24 24"><path d="M6.6 10.8a15 15 0 006.6 6.6l2.2-2.2c.3-.3.7-.4 1-.2 1.1.4 2.3.6 3.6.6.6 0 1 .4 1 1V20c0 .6-.4 1-1 1A17 17 0 013 4c0-.6.4-1 1-1h3.5c.6 0 1 .4 1 1 0 1.3.2 2.5.6 3.6.1.3 0 .7-.2 1z"/></svg><span>010-101-0101</span></li>
      <li class="contact-item contact-item--mail"><svg viewBox="0 0 24 24"><path d="M2 5h20v14H2zm2 2v.5l8 5 8-5V7zm0 3v7h16v-7l-8 5z"/></svg><span>info@wlhtimberworks.com.au/</span></li>
      <li class="contact-item contact-item--web"><svg viewBox="0 0 24 24"><path d="M12 2a10 10 0 100 20 10 10 0 000-20zm-1 2.1V8H7.4A8 8 0 0111 4.1zm2 0A8 8 0 0116.6 8H13zM5 10h6v4H5a8 8 0 010-4zm8 0h6a8 8 0 010 4h-6zm-5.6 6H11v3.9A8 8 0 017.4 16zm5.6 0h3.6a8 8 0 01-3.6 3.9z"/></svg><span>wlhtimberworks.com.au/</span></li>
      <li class="contact-item contact-item--address"><svg viewBox="0 0 24 24"><path d="M12 2a7 7 0 00-7 7c0 5 7 13 7 13s7-8 7-13a7 7 0 00-7-7zm0 9.5a2.5 2.5 0 110-5 2.5 2.5 0 010 5z"/></svg><span>Street address, zip code<br>City</span></li>
    </ul>
    <div class="social-panel">
      <div class="social-item"><div class="social-item__icon"></div>user_name</div>
      <div class="social-item"><div class="social-item__icon"></div>@username</div>
      <div class="social-item"><div class="social-item__icon"></div>@username</div>
      <div class="social-item"><div class="social-item__icon"></div>@username</div>
    </div>
  </section>

  <section class="signature signature--on-grey">
    <div class="brand-mark"><div class="brand-mark__square"></div><div class="brand-mark__name">WLH<br>Timber Works</div></div>
    <h1 class="person-name">SURENAME</h1>
    <div class="divider"></div>
    <p class="job-title">MANAGING DIRECTOR</p>
    <ul class="contact-list">
      <li class="contact-item contact-item--phone"><svg viewBox="0 0 24 24"><path d="M6.6 10.8a15 15 0 006.6 6.6l2.2-2.2c.3-.3.7-.4 1-.2 1.1.4 2.3.6 3.6.6.6 0 1 .4 1 1V20c0 .6-.4 1-1 1A17 17 0 013 4c0-.6.4-1 1-1h3.5c.6 0 1 .4 1 1 0 1.3.2 2.5.6 3.6.1.3 0 .7-.2 1z"/></svg><span>010-101-0101</span></li>
      <li class="contact-item contact-item--mail"><svg viewBox="0 0 24 24"><path d="M2 5h20v14H2zm2 2v.5l8 5 8-5V7zm0 3v7h16v-7l-8 5z"/></svg><span>info@wlhtimberworks.com.au/</span></li>
      <li class="contact-item contact-item--web"><svg viewBox="0 0 24 24"><path d="M12 2a10 10 0 100 20 10 10 0 000-20zm-1 2.1V8H7.4A8 8 0 0111 4.1zm2 0A8 8 0 0116.6 8H13zM5 10h6v4H5a8 8 0 010-4zm8 0h6a8 8 0 010 4h-6zm-5.6 6H11v3.9A8 8 0 017.4 16zm5.6 0h3.6a8 8 0 01-3.6 3.9z"/></svg><span>wlhtimberworks.com.au/</span></li>
      <li class="contact-item contact-item--address"><svg viewBox="0 0 24 24"><path d="M12 2a7 7 0 00-7 7c0 5 7 13 7 13s7-8 7-13a7 7 0 00-7-7zm0 9.5a2.5 2.5 0 110-5 2.5 2.5 0 010 5z"/></svg><span>Street address, zip code<br>City</span></li>
    </ul>
    <div class="social-panel">
      <div class="social-item"><div class="social-item__icon"></div>user_name</div>
      <div class="social-item"><div class="social-item__icon"></div>@username</div>
      <div class="social-item"><div class="social-item__icon"></div>@username</div>
      <div class="social-item"><div class="social-item__icon"></div>@username</div>
    </div>
  </section>
</body>
</html>
```